New Plumbing Company

We are looking for a smart and creative business card design for our new plumbing company. We are looking for creativity and originality in our business cards.

Industry/Entity Type

Plumbing

Contact Information for Business Card

Crestline Plumbing
Peter Halvane
Managing Director
Telephone Number : 0481529604
Email : service@crestlineplumbing.com.au
Website : www.crestlineplumbing.com.au
Lic. 508264K

Colors
0692cd
33a6d7
000000

Requirements
Must have
• I want the business card to be designed on a black background using the blue tones i have selected as seen in the company logo.

```html
<!DOCTYPE html>
<html lang="en">
<head>
<meta charset="utf-8">
<title>Crestline Plumbing – Business Card</title>
<link rel="stylesheet" href="https://fonts.googleapis.com/css2?family=Open+Sans:wght@300;400;600;700&display=swap">
<style>
  :root {
    --blue-deep: #0692cd;
    --blue-light: #33a6d7;
    --black: #000000;
    --card-black: #0b0f12;
    --white: #ffffff;
    --paper: #f4f5f6;
    --ink: #2a2a2a;
    --ink-soft: #6b6f73;
    --backdrop: #d9d6d1;
  }
  * { box-sizing: border-box; margin: 0; padding: 0; }
  html, body {
    width: 1200px; height: 1023px; overflow: hidden;
    background: var(--backdrop);
    font-family: "Open Sans", Arial, sans-serif;
  }
  .sheet {
    width: 1200px; height: 1023px;
    display: flex; flex-direction: column;
    align-items: center; justify-content: center; gap: 60px;
  }
  .card {
    position: relative; width: 700px; height: 400px;
    border-radius: 24px; overflow: hidden;
    box-shadow: 0 10px 30px rgba(0,0,0,0.25);
  }
  .card-front { background: var(--paper); }
  .card-back { background: var(--card-black); }
  .card-art { position: absolute; inset: 0; width: 100%; height: 100%; }

  .brand {
    position: absolute; display: flex; align-items: center;
    white-space: nowrap;
  }
  .brand-front {
    top: 56px; right: 35px; width: 250px;
    flex-direction: column; gap: 14px;
  }
  .brand-back {
    top: 50%; left: 50%; transform: translate(-50%, -50%); gap: 18px;
  }
  .brand-dot {
    width: 46px; height: 46px; border-radius: 50%;
    border: 4px solid var(--blue-light); flex: none;
  }
  .brand-name {
    color: var(--white); font-weight: 300; font-size: 30px;
    line-height: 1; letter-spacing: 0.3px;
  }
  .brand-back .brand-name { font-size: 46px; }
  .brand-back .brand-dot { width: 56px; height: 56px; border-width: 5px; }

  .contact {
    position: absolute; left: 46px; bottom: 36px; color: var(--ink);
  }
  .person-name {
    color: var(--blue-deep); font-weight: 700; font-size: 22px;
    text-transform: uppercase; line-height: 1.1;
  }
  .person-role { font-size: 14px; margin-bottom: 14px; }
  .contact-list { list-style: none; font-size: 14px; margin-bottom: 16px; }
  .contact-list li { display: flex; align-items: center; gap: 10px; line-height: 25px; }
  .contact-icon { width: 16px; height: 16px; flex: none; }
  .company-name { font-weight: 700; font-size: 14px; }
  .company-address { font-size: 13px; color: var(--ink-soft); line-height: 1.45; }
  .licence { font-size: 12px; color: var(--ink-soft); margin-top: 4px; }
</style>
</head>
<body>
<main class="sheet">

  <section class="card card-front" aria-label="Business card front">
    <svg class="card-art" viewBox="0 0 700 400" aria-hidden="true">
      <path d="M290 0 Q350 280 700 300 L700 0 Z" fill="var(--blue-light)"/>
      <path d="M316 0 Q372 262 700 280 L700 0 Z" fill="var(--white)"/>
      <path d="M324 0 Q380 256 700 273 L700 0 Z" fill="var(--card-black)"/>
    </svg>

    <div class="brand brand-front">
      <span class="brand-dot"></span>
      <span class="brand-name">Crestline Plumbing</span>
    </div>

    <div class="contact">
      <h1 class="person-name">Peter Halvane</h1>
      <p class="person-role">Managing Director</p>
      <ul class="contact-list">
        <li>
          <svg class="contact-icon" viewBox="0 0 16 16" aria-hidden="true">
            <circle cx="8" cy="8" r="8" fill="var(--blue-deep)"/>
            <path d="M5 4.5 L6.6 4.2 L7.3 6 L6.4 6.8 Q7.2 8.6 9.2 9.6 L10 8.7 L11.8 9.4 L11.5 11 Q7.5 11.3 5 6.5 Z" fill="var(--white)"/>
          </svg>
          <span>0481529604</span>
        </li>
        <li>
          <svg class="contact-icon" viewBox="0 0 16 16" aria-hidden="true">
            <circle cx="8" cy="8" r="8" fill="var(--blue-deep)"/>
            <rect x="4" y="5.2" width="8" height="5.6" rx="0.6" fill="none" stroke="var(--white)" stroke-width="1.1"/>
            <path d="M4.3 5.6 L8 8.4 L11.7 5.6" fill="none" stroke="var(--white)" stroke-width="1.1"/>
          </svg>
          <span>service@crestlineplumbing.com.au</span>
        </li>
        <li>
          <svg class="contact-icon" viewBox="0 0 16 16" aria-hidden="true">
            <circle cx="8" cy="8" r="8" fill="var(--blue-deep)"/>
            <circle cx="8" cy="8" r="4.2" fill="none" stroke="var(--white)" stroke-width="1"/>
            <ellipse cx="8" cy="8" rx="1.8" ry="4.2" fill="none" stroke="var(--white)" stroke-width="1"/>
            <line x1="3.8" y1="8" x2="12.2" y2="8" stroke="var(--white)" stroke-width="1"/>
          </svg>
          <span>www.crestlineplumbing.com.au</span>
        </li>
      </ul>
      <p class="company-name">Crestline Plumbing Ltd.</p>
      <p class="company-address">48 Harbour Street<br>Eastvale, Any City</p>
      <p class="licence">Lic. 508264K</p>
    </div>
  </section>

  <section class="card card-back" aria-label="Business card back">
    <div class="brand brand-back">
      <span class="brand-dot"></span>
      <span class="brand-name">Crestline Plumbing</span>
    </div>
  </section>

</main>
</body>
</html>
```